Verostel business card

Business card for sustainable investment company called "Verostel". Verostel is an exchange platform selling carbon credits between buyers and sellers. Carbon Credits are an environmental commodity for reducing global carbon emissions.

the card should obviously have our logo and the theme should be sustainability/environment mixed with a trading platform.

Contact Information for Business Card

Logo, Name, Title, Phone, Email

Colors
0054AA
0677BA
7BADD7
CADEEF
E8F1F8
0094D4
00A9DD
6FCCEA
C7EBF8
E9F6FB
00AB8E
00BBA5
67D7C9
C6EFE9
E9F9F6
59FF00
82FF00
B8FF75
E3FFCB
F4FFEA

```html
<!DOCTYPE html>
<html lang="en">
<head>
<meta charset="utf-8">
<title>Verostel business card</title>
<link href="https://fonts.googleapis.com/css2?family=Figtree:wght@400;500;700;800&display=swap" rel="stylesheet">
<style>
  :root {
    --canvas-bg: #969696;
    --card-front: #ebebeb;
    --card-back: #0d2a52;
    --navy: #0d2a52;
    --muted: #8a8a8a;
    --contact: #777777;
    --cyan: #2fd8f2;
    --blue: #1e7cf5;
    --white: #ffffff;
  }
  html, body {
    margin: 0;
    padding: 0;
    width: 1200px;
    height: 1000px;
    overflow: hidden;
    background: var(--canvas-bg);
    font-family: "Figtree", Arial, sans-serif;
  }
  .canvas { position: relative; width: 1200px; height: 1000px; }
  .card {
    position: absolute;
    width: 615px;
    height: 351px;
    border-radius: 28px;
    overflow: hidden;
  }
  .card--front { left: 293px; top: 80px; background: var(--card-front); }
  .card--back { left: 286px; top: 493px; background: var(--card-back); }

  .brand {
    position: absolute;
    left: 60px;
    top: 140px;
    width: 260px;
    display: flex;
    align-items: center;
    justify-content: center;
    gap: 12px;
  }
  .brand__dot {
    width: 26px; height: 26px; border-radius: 50%;
    background: var(--blue);
  }
  .brand__name {
    font-weight: 800;
    font-size: 44px;
    letter-spacing: 0.5px;
    color: var(--navy);
    line-height: 1;
  }

  .contact {
    position: absolute;
    left: 350px;
    top: 112px;
    width: 200px;
    text-align: center;
  }
  .contact__name {
    font-weight: 700; font-size: 21px; color: var(--navy);
    letter-spacing: 0.5px; line-height: 26px;
  }
  .contact__title {
    font-size: 18px; color: var(--muted); letter-spacing: 0.5px; line-height: 22px;
  }
  .contact__icons {
    display: flex; justify-content: center; gap: 6px; margin: 10px 0 8px;
  }
  .icon {
    width: 33px; height: 33px; border-radius: 50%;
    background: linear-gradient(135deg, var(--cyan), var(--blue));
    display: flex; align-items: center; justify-content: center;
  }
  .icon svg { width: 16px; height: 16px; }
  .contact__line {
    font-size: 16.5px; color: var(--contact); letter-spacing: 0.8px; line-height: 23px;
  }

  .back__name {
    position: absolute;
    right: 66px;
    top: 274px;
    font-weight: 700;
    font-size: 37px;
    color: var(--white);
    letter-spacing: 0.3px;
    line-height: 1;
  }
</style>
</head>
<body>
<div class="canvas">
  <section class="card card--front">
    <div class="brand">
      <span class="brand__dot"></span>
      <span class="brand__name">VEROSTEL</span>
    </div>
    <div class="contact">
      <div class="contact__name">Name Surname</div>
      <div class="contact__title">Title</div>
      <div class="contact__icons">
        <span class="icon" aria-label="Phone">
          <svg viewBox="0 0 24 24"><path fill="#fff" d="M6.6 10.8a15 15 0 0 0 6.6 6.6l2.2-2.2c.3-.3.7-.4 1-.2 1.1.4 2.3.6 3.6.6.6 0 1 .4 1 1V20c0 .6-.4 1-1 1C10.6 21 3 13.4 3 4c0-.6.4-1 1-1h3.5c.6 0 1 .4 1 1 0 1.3.2 2.5.6 3.6.1.3 0 .7-.2 1z"/></svg>
        </span>
        <span class="icon" aria-label="Email">
          <svg viewBox="0 0 24 24"><rect x="3" y="5.5" width="18" height="13" rx="1.5" fill="#fff"/><path d="M3.5 6.5 12 13l8.5-6.5" fill="none" stroke="#1e9cf5" stroke-width="1.5"/></svg>
        </span>
        <span class="icon" aria-label="Website">
          <svg viewBox="0 0 24 24" fill="none" stroke="#fff" stroke-width="1.6"><circle cx="12" cy="12" r="8.5"/><ellipse cx="12" cy="12" rx="3.8" ry="8.5"/><path d="M3.5 12h17M5 7.5h14M5 16.5h14"/></svg>
        </span>
      </div>
      <div class="contact__line">012•345•6789</div>
      <div class="contact__line">name@website.com</div>
      <div class="contact__line">website.com</div>
    </div>
  </section>

  <section class="card card--back">
    <div class="back__name">VEROSTEL</div>
  </section>
</div>
</body>
</html>
```